Powerpoint and Word Document Template

Our target market are C-suite executives in banks, credit unions, non-bank financial institutions, financial technology companies and in the law firms, private equity firms and the like that are also advising the industry.

design should convey: confidence, trust, expertise, experience, value, advice, relationship focus.

For the stationery design, we will need the .doc format as well.

Industry/Entity Type

Consulting

Font styles to use
Sans Serif

Colors
0356a4
3277b5
85acd3
cedeed
eaf1f7
ffffff

Requirements
Must have
• must use the logo and color scheme included in the attached zip file. must include a powerpoint template with a cover slide, section break slides, slides for images/graphics, slides for side by side content, and slides for regular content.

Note: this should also include designs for word documents like stationary and envelopes based on the same concept.

```html
<!DOCTYPE html>
<html lang="en">
<head>
<meta charset="utf-8">
<title>Vantrel Advisory – 20-Slide Presentation Template</title>
<link href="https://fonts.googleapis.com/css2?family=Montserrat:wght@400;500;600;700;800&display=swap" rel="stylesheet">
<style>
:root{
  --navy:#1d3a6e;
  --navy-deep:#17305c;
  --blue:#0356a4;
  --mid:#3277b5;
  --sky:#85acd3;
  --pale:#cedeed;
  --mist:#eaf1f7;
  --white:#ffffff;
  --board:#4a4a4a;
  --ink:#1f2a3a;
  --red:#e0393e;
}
*{box-sizing:border-box;margin:0;padding:0}
html,body{width:1200px;height:731px;overflow:hidden;background:var(--board)}
body{font-family:'Montserrat',sans-serif;position:relative;color:var(--white)}

/* header */
.brand{position:absolute;left:16px;top:50px;display:flex;align-items:center;gap:8px}
.brand-square{width:30px;height:30px;border:2px solid var(--white)}
.brand-name{font-weight:600;font-size:22px;letter-spacing:1px;line-height:1}
.brand-sub{font-size:8px;letter-spacing:3px;text-align:center;margin-top:2px}
.divider{position:absolute;width:1px;background:#8a8a8a}
.board-title{position:absolute;left:198px;top:52px;font-size:24px;font-weight:600;color:var(--pale);letter-spacing:.3px}
.note{position:absolute;left:560px;top:31px;width:610px;font-size:13.2px;line-height:15.5px;color:#dcdcdc}
.note b{color:var(--white)}

/* slide frame */
.slide{position:absolute;width:217px;height:122px;overflow:hidden;background:var(--white);box-shadow:0 0 0 1px #ccc}
.c1{left:12px}.c2{left:247px}.c3{left:481px}.c4{left:714px}.c5{left:949px}
.r1{top:112px}.r2{top:251px}.r3{top:392px}.r4{top:535px}
.abs{position:absolute}
.photo{position:absolute}
.navy{background:var(--navy)}
.tiny{font-size:3.2px;line-height:4.2px;color:var(--ink)}
.tiny.light{color:var(--pale)}
.logo-mini{position:absolute;display:flex;align-items:center;gap:2px;font-size:5px;font-weight:700;letter-spacing:.4px;color:var(--white)}
.logo-mini i{display:block;width:5px;height:5px;border:1px solid currentColor}
.logo-mini.dark{color:var(--navy)}
.title-bar{position:absolute;left:0;top:0;width:100%;height:9px;background:var(--mid)}
.title-bar span{position:absolute;left:6px;top:2px;font-size:4.2px;font-weight:800;color:var(--white);letter-spacing:.3px}
.title-bar .logo-mini{right:5px;top:2px;left:auto;font-size:3.6px}
.foot{position:absolute;left:6px;bottom:3px;font-size:2.6px;color:var(--navy)}
.pg{position:absolute;right:4px;bottom:3px;width:6px;height:5px;background:var(--mid);font-size:3px;color:#fff;text-align:center;line-height:5px}
.sec-num{font-size:8.5px;font-weight:700;letter-spacing:1.6px;color:var(--white)}
.sec-sub{font-size:4px;letter-spacing:.8px;color:var(--pale)}
.sub-h{font-size:4px;font-weight:700;color:var(--blue)}
.plus{position:absolute;width:5px;height:5px;border:.6px solid var(--red);color:var(--red);font-size:4.5px;line-height:3.6px;text-align:center}

/* footer */
.specs{position:absolute;top:690px;left:0;width:1200px;height:26px;display:flex;align-items:center;font-size:20px;font-weight:700;color:#cfcfcf}
.specs span{padding:0 14px;border-left:1px solid #7d7d7d;white-space:nowrap}
.specs span:first-child{padding-left:14px;border-left:none}
</style>
</head>
<body>

<header>
  <div class="brand">
    <div class="brand-square"></div>
    <div>
      <div class="brand-name">VANTREL</div>
      <div class="brand-sub">ADVISORY</div>
    </div>
  </div>
  <div class="divider" style="left:178px;top:32px;height:62px"></div>
  <h1 class="board-title">20-SLIDE PPT TEMPLATE</h1>
  <div class="divider" style="left:550px;top:32px;height:62px"></div>
  <p class="note"><b>Note from Designer:</b> All slide-layouts have been designed; some slides are still being updated with sample images, and/or infographics. Expect update soon. Please provide feedback on overall direction, any revisions you want, and any other detail you might want to comment on. Thank you</p>
</header>

<main>
<!-- 1 Cover -->
<section class="slide c1 r1">
  <div class="photo" role="img" aria-label="Soft faded photo of a business newspaper" style="left:0;top:70px;width:217px;height:52px;background:linear-gradient(180deg,rgba(255,255,255,1),#d3dbe6)"></div>
  <div class="logo-mini dark" style="left:88px;top:27px;font-size:6px"><i></i>VANTREL</div>
  <div class="abs" style="left:0;width:217px;top:50px;text-align:center;font-size:9.5px;font-weight:800;color:var(--blue);line-height:11px">CORPORATE<br>PRESENTATION</div>
  <div class="abs" style="left:0;width:217px;top:74px;text-align:center;font-size:4.5px;font-weight:600;letter-spacing:1.5px;color:var(--navy)">TEMPLATE</div>
</section>

<!-- 2 Contents -->
<section class="slide c2 r1">
  <div class="photo" role="img" aria-label="Photo of a folded business newspaper" style="left:0;top:0;width:130px;height:122px;background:linear-gradient(135deg,#dfe4ea,#9aa6b6)"></div>
  <div class="abs" style="left:0;top:12px;width:40px;height:14px;background:var(--mid)"><div class="logo-mini" style="left:6px;top:4px"><i></i>VANTREL</div></div>
  <div class="abs navy" style="left:122px;top:0;width:95px;height:112px"></div>
  <div class="abs" style="left:0;top:112px;width:217px;height:10px;background:var(--navy-deep)"></div>
  <div class="abs" style="left:130px;top:16px;font-size:5px;font-weight:700">CONTENTS</div>
  <div class="abs tiny light" style="left:130px;top:26px;width:82px">
    <b style="color:#fff">SECTION 01: Image/Graphic Slides</b><br>01 Sample slide name<br>02 Sample slide name<br>03 Sample slide name<br>
    <b style="color:#fff">SECTION 02: Side by Side Content</b><br>04 Sample slide name<br>05 Sample slide name<br>
    <b style="color:#fff">SECTION 03: Regular Content</b><br>06 Sample slide name<br>07 Sample slide name<br>
    <b style="color:#fff">SECTION 04: Special Slides</b><br>08 Sample slide name<br>09 Sample slide name
  </div>
  <div class="pg" style="bottom:2px">02</div>
</section>

<!-- 3 Section 01 -->
<section class="slide c3 r1 navy">
  <div class="abs" style="left:0;top:112px;width:217px;height:10px;background:var(--blue)"></div>
  <div class="abs" style="left:32px;top:30px"><div class="sec-num">SECTION 01</div><div class="sec-sub">IMAGE/GRAPHICS SLIDES</div></div>
  <div class="photo" role="img" aria-label="Photo of printed charts and graphs on a desk" style="left:32px;top:56px;width:94px;height:56px;background:linear-gradient(135deg,#f1f1f1,#d9c8c8)"></div>
  <div class="abs" style="left:34px;top:108px;width:40px;height:10px;background:var(--white)"></div>
  <div class="logo-mini dark" style="left:37px;top:110px"><i></i>VANTREL</div>
</section>

<!-- 4 Line chart -->
<section class="slide c4 r1">
  <div class="abs" style="left:6px;top:4px;font-size:5.5px;font-weight:700;color:var(--navy)">Image/Graphic Title_</div>
  <div class="logo-mini dark" style="right:6px;left:auto;top:5px;font-size:3.6px"><i></i>VANTREL</div>
  <div class="abs" style="left:0;top:14px;width:78px;height:76px;background:var(--mist)"></div>
  <div class="abs" style="left:28px;top:24px;width:2px;height:12px;background:var(--blue)"></div>
  <div class="abs tiny" style="left:32px;top:24px;width:42px;color:var(--blue)">Sample key point here in a short line.</div>
  <div class="abs" style="left:28px;top:50px;width:48px;height:14px;border:.8px solid var(--blue);background:#fff"></div>
  <div class="abs" style="left:33px;top:52px;font-size:6px;font-weight:800;color:var(--navy)">25% Y/Y</div>
  <div class="abs tiny" style="left:33px;top:59px;font-size:2.6px">Sample growth note</div>
  <svg class="abs" style="left:88px;top:18px" width="120" height="66" viewBox="0 0 120 66">
    <g stroke="#dde4ee" stroke-width=".4"><line x1="0" y1="6" x2="120" y2="6"/><line x1="0" y1="20" x2="120" y2="20"/><line x1="0" y1="34" x2="120" y2="34"/><line x1="0" y1="48" x2="120" y2="48"/><line x1="0" y1="60" x2="120" y2="60"/></g>
    <polyline fill="none" stroke="#3277b5" stroke-width="1" points="2,44 12,30 22,50 32,34 42,40 52,24 62,36 72,20 82,44 92,30 102,40 112,36 118,6"/>
    <polyline fill="none" stroke="#85acd3" stroke-width="1" points="2,50 12,46 22,40 32,50 42,46 52,44 62,48 72,38 82,42 92,40 102,36 112,32 118,30"/>
    <g fill="#3277b5"><circle cx="72" cy="20" r="1.2"/><circle cx="118" cy="6" r="1.2"/><circle cx="52" cy="24" r="1.2"/></g>
  </svg>
  <div class="abs navy" style="left:0;top:90px;width:217px;height:32px"></div>
  <div class="abs tiny light" style="left:6px;top:94px;width:60px">Brief supporting copy goes here in short lines for this chart.</div>
  <div class="abs tiny light" style="left:70px;top:94px;width:60px">Brief supporting copy goes here in short lines for this chart.</div>
  <div class="logo-mini" style="left:180px;top:97px;font-size:3.6px"><i></i>VANTREL</div>
  <div class="pg" style="background:var(--sky)">04</div>
</section>

<!-- 5 Full photo -->
<section class="slide c5 r1 navy">
  <div class="photo" role="img" aria-label="Photo of two colleagues reviewing documents at a laptop" style="left:0;top:0;width:217px;height:112px;background:linear-gradient(120deg,#e9eef4 0%,#b8c6d8 45%,#47689a 100%)"></div>
  <svg class="abs" style="left:0;top:0" width="217" height="122" viewBox="0 0 217 122"><path d="M0 0 H60 Q30 60 80 122 H0 Z" fill="#1d3a6e"/><path d="M150 0 H217 V122 H140 Q190 60 150 0Z" fill="#1d3a6e" opacity=".55"/></svg>
  <div class="logo-mini" style="left:6px;top:8px"><i></i>VANTREL</div>
  <div class="abs tiny light" style="left:6px;top:80px;width:44px">Brief supporting copy goes here in short lines.</div>
  <div class="abs" style="left:170px;top:36px;font-size:7px;font-weight:700;line-height:8.5px">Image/<br>Graphic<br>Title_</div>
  <div class="abs" style="left:0;top:116px;width:217px;height:6px;background:var(--blue)"></div>
</section>

<!-- 6 Photo + stats -->
<section class="slide c1 r2 navy">
  <div class="photo" role="img" aria-label="Aerial photo of a busy city festival crowd" style="left:0;top:0;width:157px;height:92px;background:linear-gradient(160deg,#8fa2b8,#c59a6a 50%,#5c7ea6)"></div>
  <div class="abs" style="left:6px;top:5px;font-size:5.5px;font-weight:700">Image/Graphic Title_</div>
  <div class="abs" style="left:157px;top:0;width:60px;height:92px;background:var(--blue)"></div>
  <div class="abs tiny" style="left:162px;top:6px;color:#fff;font-weight:700">Key figures overview</div>
  <div class="abs" style="left:162px;top:16px;font-size:3.4px;line-height:9px;color:#fff;font-weight:700">25% growth<br>$120k value<br>$3.5b assets<br>2.7m clients</div>
  <div class="abs tiny light" style="left:6px;top:96px;width:48px">Brief supporting copy goes here in short lines.</div>
  <div class="abs tiny light" style="left:60px;top:96px;width:48px">Brief supporting copy goes here in short lines.</div>
  <div class="abs tiny light" style="left:114px;top:96px;width:48px">Brief supporting copy goes here in short lines.</div>
  <div class="logo-mini" style="left:183px;top:100px;font-size:3.6px"><i></i>VANTREL</div>
</section>

<!-- 7 Section 02 -->
<section class="slide c2 r2 navy">
  <div class="abs" style="left:0;top:112px;width:217px;height:10px;background:var(--blue)"></div>
  <div class="abs" style="left:130px;top:38px;text-align:right"><div class="sec-num">SECTION 02</div><div class="sec-sub">SIDE-BY-SIDE SLIDES</div></div>
  <div class="photo" role="img" aria-label="Photo of hands writing in a notebook" style="left:108px;top:58px;width:120px;height:60px;background:linear-gradient(135deg,#d9b89a,#f0ece8 60%,#c4cedb)"></div>
  <div class="abs" style="left:148px;top:108px;width:40px;height:10px;background:var(--white)"></div>
  <div class="logo-mini dark" style="left:151px;top:110px"><i></i>VANTREL</div>
</section>

<!-- 8 Bar charts -->
<section class="slide c3 r2">
  <div class="title-bar"><span>THE SLIDE TITLE</span><div class="logo-mini"><i></i>VANTREL</div></div>
  <div class="abs" style="left:6px;top:14px;width:108px;height:92px;background:var(--mist)"></div>
  <div class="abs" style="left:10px;top:18px;width:30px;height:70px;background:var(--white)"></div>
  <svg class="abs" style="left:12px;top:20px" width="26" height="66" viewBox="0 0 26 66"><g fill="#3277b5"><circle cx="13" cy="11" r="6"/><circle cx="13" cy="33" r="6"/><circle cx="13" cy="55" r="6"/></g></svg>
  <svg class="abs" style="left:44px;top:20px" width="68" height="66" viewBox="0 0 68 66">
    <g fill="#0356a4"><rect x="4" y="12" width="3" height="18"/><rect x="10" y="8" width="3" height="22"/><rect x="16" y="14" width="3" height="16"/><rect x="22" y="6" width="3" height="24"/><rect x="28" y="10" width="3" height="20"/>
    <rect x="36" y="8" width="3" height="22"/><rect x="42" y="12" width="3" height="18"/><rect x="48" y="4" width="3" height="26"/><rect x="54" y="14" width="3" height="16"/><rect x="60" y="9" width="3" height="21"/>
    <rect x="4" y="44" width="3" height="20"/><rect x="10" y="38" width="3" height="26"/><rect x="16" y="46" width="3" height="18"/><rect x="22" y="40" width="3" height="24"/><rect x="28" y="42" width="3" height="22"/>
    <rect x="36" y="40" width="3" height="24"/><rect x="42" y="44" width="3" height="20"/><rect x="48" y="36" width="3" height="28"/><rect x="54" y="46" width="3" height="18"/><rect x="60" y="41" width="3" height="23"/></g>
  </svg>
  <div class="abs" style="left:12px;top:92px;font-size:5px;font-weight:800;color:var(--navy)">2ED PTS</div>
  <div class="abs" style="left:64px;top:92px;font-size:5px;font-weight:800;color:var(--navy)">20% MSR</div>
  <div class="abs" style="left:120px;top:14px;width:90px;font-size:4.2px;font-weight:700;color:var(--blue)">Lorem ipsum dolor sit amet euismod nibh.</div>
  <div class="abs tiny" style="left:120px;top:26px;width:44px">Brief supporting copy goes here in short lines for this slide. Brief supporting copy goes here in short lines. Sample key point. Sample key point. Sample key point.</div>
  <div class="abs tiny" style="left:168px;top:26px;width:44px">Sample key point. Sample key point. Brief supporting copy goes here in short lines for this slide. Sample key point.</div>
  <div class="foot">Regular content slide / sample footer text</div><div class="pg">08</div>
</section>

<!-- 9 Diagram -->
<section class="slide c4 r2">
  <div class="title-bar" style="width:140px"><span>THE SLIDE TITLE</span></div>
  <div class="abs navy" style="left:140px;top:0;width:77px;height:122px"></div>
  <div class="logo-mini" style="left:190px;top:2px;font-size:3.6px"><i></i>VANTREL</div>
  <svg class="abs" style="left:20px;top:24px" width="100" height="60" viewBox="0 0 100 60">
    <g stroke="#3277b5" stroke-width=".7" fill="none"><line x1="30" y1="10" x2="50" y2="10"/><line x1="50" y1="10" x2="70" y2="10"/><line x1="20" y1="18" x2="14" y2="30"/><line x1="80" y1="18" x2="86" y2="30"/><line x1="50" y1="18" x2="50" y2="30"/></g>
    <g fill="#fff" stroke="#0356a4" stroke-width="1"><circle cx="22" cy="10" r="8"/><circle cx="50" cy="10" r="8"/><circle cx="78" cy="10" r="8"/><circle cx="12" cy="36" r="7"/><circle cx="88" cy="36" r="7"/></g>
    <circle cx="50" cy="38" r="8" fill="#0356a4"/>
  </svg>
  <div class="abs" style="left:36px;top:88px;font-size:5px;font-weight:700;color:var(--navy)">Our Financial Advisory</div>
  <div class="abs" style="left:148px;top:14px;font-size:3.6px;line-height:4.4px;color:#fff;width:62px">
    <b>Strategy</b><br><span style="color:var(--pale)">Brief supporting copy here.</span><br><br>
    <b>Risk Management</b><br><span style="color:var(--pale)">Brief supporting copy here.</span><br><br>
    <b>Research</b><br><span style="color:var(--pale)">Brief supporting copy here.</span><br><br>
    <b>Analysis</b><br><span style="color:var(--pale)">Brief supporting copy here.</span><br><br>
    <b>Control</b><br><span style="color:var(--pale)">Brief supporting copy here.</span>
  </div>
  <div class="foot">Regular content slide / sample footer text</div>
</section>

<!-- 10 Steps -->
<section class="slide c5 r2">
  <div class="title-bar"><span>THE SLIDE TITLE</span><div class="logo-mini"><i></i>VANTREL</div></div>
  <div class="abs" style="left:6px;top:13px;width:36px;font-size:4.4px;font-weight:700;color:var(--blue)">Lorem ipsum dolor sit amet.</div>
  <div class="abs tiny" style="left:6px;top:28px;width:36px">Sample key point. Sample key point. Sample key point. Sample key point. Sample key point. Sample key point.</div>
  <div class="abs" style="left:76px;top:9px;width:44px;height:113px;background:var(--pale)"></div>
  <div class="abs navy" style="left:120px;top:9px;width:97px;height:113px"></div>
  <div class="abs" style="left:168px;top:14px;font-size:3.6px;line-height:4.4px;color:#fff;width:44px">
    <b>Step 01</b><br><span style="color:var(--pale)">Brief supporting copy here in short lines.</span><br>
    <b>Step 02</b><br><span style="color:var(--pale)">Brief supporting copy here in short lines.</span><br>
    <b>Step 03</b><br><span style="color:var(--pale)">Brief supporting copy here in short lines.</span><br>
    <b>Step 04</b><br><span style="color:var(--pale)">Brief supporting copy here in short lines.</span>
  </div>
  <div class="foot" style="color:#fff">Regular content slide / sample footer</div>
</section>

<!-- 11 Three values -->
<section class="slide c1 r3">
  <div class="title-bar"><span>THE SLIDE TITLE</span><div class="logo-mini"><i></i>VANTREL</div></div>
  <div class="abs" style="left:6px;top:26px;width:52px;font-size:3.6px;line-height:4.6px;color:var(--ink)">
    <b style="color:var(--blue);font-size:4.2px">Our Professionalism.</b><br>Brief supporting copy here in short lines.<br><br>
    <b style="color:var(--blue);font-size:4.2px">Our Modern Approach.</b><br>Brief supporting copy here in short lines.<br><br>
    <b style="color:var(--blue);font-size:4.2px">Our Expertise.</b><br>Brief supporting copy here in short lines.
  </div>
  <div class="abs" style="left:112px;top:9px;width:105px;height:104px;background:var(--blue)"></div>
  <div class="abs" style="left:112px;top:9px;width:40px;height:104px;background:var(--navy)"></div>
  <svg class="abs" style="left:122px;top:16px" width="20" height="90" viewBox="0 0 20 90"><line x1="10" y1="10" x2="10" y2="80" stroke="#85acd3" stroke-width=".6"/><g fill="#fff"><circle cx="10" cy="10" r="6"/><circle cx="10" cy="45" r="6"/><circle cx="10" cy="80" r="6"/></g></svg>
  <div class="abs" style="left:156px;top:36px;font-size:6.2px;font-weight:700;line-height:7.2px;color:#fff">future-proof,<br>satisfying &amp;<br>value-adding<br><span style="font-weight:500">financial<br>advisory you<br>can trust</span></div>
  <div class="abs" style="left:180px;top:88px;width:24px;height:25px;background:var(--mist)"></div>
  <div class="foot">Regular content slide / sample footer text</div><div class="pg">11</div>
</section>

<!-- 12 Section 03 -->
<section class="slide c2 r3 navy">
  <div class="abs" style="left:32px;top:32px"><div class="sec-num">SECTION 03</div><div class="sec-sub">REGULAR CONTENT SLIDES</div></div>
  <div class="abs" style="left:32px;top:62px;width:94px;height:60px;background:var(--mist)"></div>
  <div class="logo-mini dark" style="left:38px;top:110px"><i></i>VANTREL</div>
</section>

<!-- 13 Four text columns -->
<section class="slide c3 r3">
  <div class="title-bar"><span>THE SLIDE TITLE</span><div class="logo-mini"><i></i>VANTREL</div></div>
  <div class="abs" style="left:12px;top:14px;width:200px;display:grid;grid-template-columns:repeat(4,1fr);gap:4px 6px">
    <div><div class="sub-h">Subtitle One</div><div class="tiny">Brief supporting copy goes here in short lines for this column.</div></div>
    <div><div class="sub-h">&nbsp;</div><div class="tiny">Brief supporting copy goes here in short lines for this column.</div></div>
    <div><div class="sub-h">Subtitle Two</div><div class="tiny">Brief supporting copy goes here in short lines for this column.</div></div>
    <div><div class="sub-h">&nbsp;</div><div class="tiny">Brief supporting copy goes here in short lines for this column.</div></div>
    <div><div class="sub-h">Subtitle Three</div><div class="tiny">Brief supporting copy goes here in short lines for this column.</div></div>
    <div><div class="sub-h">&nbsp;</div><div class="tiny">Brief supporting copy goes here in short lines for this column.</div></div>
    <div><div class="sub-h">Subtitle Four</div><div class="tiny">Brief supporting copy goes here in short lines for this column.</div></div>
    <div><div class="sub-h">&nbsp;</div><div class="tiny">Brief supporting copy goes here in short lines for this column.</div></div>
  </div>
  <div class="plus" style="left:68px;top:52px">+</div><div class="plus" style="left:138px;top:52px">+</div><div class="plus" style="left:204px;top:52px">+</div>
  <div class="plus" style="left:68px;top:100px">+</div><div class="plus" style="left:138px;top:100px">+</div><div class="plus" style="left:204px;top:100px">+</div>
  <div class="foot">Regular content slide / sample footer text</div><div class="pg">13</div>
</section>

<!-- 14 Blocks -->
<section class="slide c4 r3">
  <div class="title-bar"><span>THE SLIDE TITLE</span><div class="logo-mini"><i></i>VANTREL</div></div>
  <div class="abs navy" style="left:6px;top:16px;width:42px;height:36px"></div>
  <div class="abs navy" style="left:6px;top:62px;width:42px;height:46px"></div>
  <div class="abs" style="left:52px;top:16px;width:20px;height:36px;background:var(--sky)"></div>
  <div class="abs" style="left:88px;top:64px;width:22px;height:44px;background:var(--sky)"></div>
  <div class="abs" style="left:110px;top:16px;width:100px;height:36px;background:var(--sky)"></div>
  <div class="abs" style="left:76px;top:16px;width:32px"><div class="sub-h">Subtitle One</div><div class="tiny">Brief supporting copy goes here in short lines.</div></div>
  <div class="abs" style="left:52px;top:62px;width:34px"><div class="sub-h">Subtitle One</div><div class="tiny">Brief supporting copy goes here in short lines.</div></div>
  <div class="abs" style="left:114px;top:62px;width:96px"><div class="sub-h">Lorem ipsum dolor sit amet euismod nibh.</div><div class="tiny">Brief supporting copy goes here in short lines for this slide. Brief supporting copy goes here in short lines.</div></div>
  <div class="foot">Regular content slide / sample footer text</div><div class="pg">14</div>
</section>

<!-- 15 Block grid -->
<section class="slide c5 r3">
  <div class="title-bar"><span>THE SLIDE TITLE</span><div class="logo-mini"><i></i>VANTREL</div></div>
  <div class="abs" style="left:6px;top:14px;width:30px;height:28px;background:var(--pale)"></div>
  <div class="abs" style="left:96px;top:14px;width:28px;height:28px;background:var(--pale)"></div>
  <div class="abs" style="left:6px;top:48px;width:28px;height:30px;background:var(--pale)"></div>
  <div class="abs" style="left:184px;top:48px;width:28px;height:30px;background:var(--pale)"></div>
  <div class="abs" style="left:6px;top:84px;width:28px;height:28px;background:var(--pale)"></div>
  <div class="abs" style="left:118px;top:84px;width:28px;height:28px;background:var(--pale)"></div>
  <div class="abs" style="left:40px;top:14px;width:40px"><div class="sub-h">Subtitle One</div><div class="tiny">Brief supporting copy here in short lines.</div></div>
  <div class="abs" style="left:128px;top:14px;width:40px"><div class="sub-h">Subtitle One</div><div class="tiny">Brief supporting copy here in short lines.</div></div>
  <div class="abs" style="left:40px;top:48px;width:40px"><div class="sub-h">Subtitle One</div><div class="tiny">Brief supporting copy here in short lines.</div></div>
  <div class="abs" style="left:140px;top:48px;width:40px"><div class="sub-h">Subtitle One</div><div class="tiny">Brief supporting copy here in short lines.</div></div>
  <div class="abs" style="left:40px;top:84px;width:40px"><div class="sub-h">Subtitle One</div><div class="tiny">Brief supporting copy here in short lines.</div></div>
  <div class="abs" style="left:150px;top:84px;width:40px"><div class="sub-h">Subtitle One</div><div class="tiny">Brief supporting copy here in short lines.</div></div>
  <div class="plus" style="left:84px;top:36px">+</div><div class="plus" style="left:208px;top:36px">+</div><div class="plus" style="left:84px;top:72px">+</div><div class="plus" style="left:208px;top:72px">+</div>
  <div class="foot">Regular content slide / sample footer text</div><div class="pg">15</div>
</section>

<!-- 16 Steps with longer subtitle -->
<section class="slide c1 r4">
  <div class="title-bar"><span>THE SLIDE TITLE</span><div class="logo-mini"><i></i>VANTREL</div></div>
  <div class="abs navy" style="left:6px;top:16px;width:38px;height:26px"></div>
  <div class="abs navy" style="left:6px;top:48px;width:38px;height:26px"></div>
  <div class="abs navy" style="left:6px;top:80px;width:38px;height:26px"></div>
  <div class="abs" style="left:44px;top:16px;width:42px;height:26px;background:var(--mist)"></div>
  <div class="abs" style="left:44px;top:48px;width:42px;height:26px;background:var(--mist)"></div>
  <div class="abs" style="left:44px;top:80px;width:42px;height:26px;background:var(--mist)"></div>
  <div class="abs" style="left:10px;top:19px;font-size:3.6px;font-weight:700">Step 01</div>
  <div class="abs" style="left:10px;top:51px;font-size:3.6px;font-weight:700">Step 02</div>
  <div class="abs" style="left:10px;top:83px;font-size:3.6px;font-weight:700">Step 03</div>
  <div class="abs" style="left:92px;top:14px;width:56px"><div class="sub-h">Here is a much longer subtitle.</div><div class="tiny">Brief supporting copy goes here in short lines for this slide.</div></div>
  <div class="abs" style="left:154px;top:20px;width:56px"><div class="tiny">Brief supporting copy goes here in short lines for this slide.</div></div>
  <div class="abs" style="left:92px;top:44px;width:56px"><div class="sub-h">Here is a much longer subtitle.</div><div class="tiny">Brief supporting copy goes here in short lines for this slide.</div></div>
  <div class="abs" style="left:154px;top:44px;width:56px;height:20px;background:var(--mist)"></div>
  <div class="abs" style="left:92px;top:78px;width:56px"><div class="sub-h">Here is a much longer subtitle.</div><div class="tiny">Brief supporting copy goes here in short lines for this slide.</div></div>
  <div class="abs" style="left:154px;top:82px;width:56px"><div class="tiny">Brief supporting copy goes here in short lines for this slide.</div></div>
  <div class="foot">Regular content slide / sample footer text</div><div class="pg">16</div>
</section>

<!-- 17 Section 04 -->
<section class="slide c2 r4 navy">
  <div class="abs" style="left:0;top:112px;width:217px;height:10px;background:var(--blue)"></div>
  <div class="abs" style="left:128px;top:34px;text-align:right"><div class="sec-num">SECTION 04</div><div class="sec-sub">SPECIAL SLIDES</div></div>
  <div class="abs" style="left:118px;top:58px;width:94px;height:64px;background:var(--pale)"></div>
  <div class="logo-mini dark" style="left:124px;top:110px"><i></i>VANTREL</div>
</section>

<!-- 18 Break -->
<section class="slide c3 r4" style="background:var(--mist)">
  <div class="photo" role="img" aria-label="Photo of an hourglass on pebbles in blue tones" style="left:6px;top:6px;width:205px;height:98px;background:linear-gradient(180deg,#4d6f9c,#2a4a78 60%,#8ea9c8)"></div>
  <div class="logo-mini" style="left:14px;top:14px"><i></i>VANTREL</div>
  <div class="abs" style="left:0;width:217px;top:56px;text-align:center;font-size:7px;font-weight:700;letter-spacing:1.2px">BREAK</div>
  <div class="abs" style="left:6px;top:104px;width:205px;height:14px;background:var(--sky)"></div>
  <div class="abs" style="left:12px;top:108px;font-size:3px;color:var(--navy);display:flex;gap:12px">
    <span>12 Harbor Lane, Suite 4</span><span>hello@vantreladvisory.com</span><span>+1 (555) 010-2040</span><span>vantreladvisory.com</span>
  </div>
</section>

<!-- 19 Thank you -->
<section class="slide c4 r4" style="background:var(--mist)">
  <div class="photo" role="img" aria-label="Photo of a person working at a laptop in blue tones" style="left:6px;top:6px;width:205px;height:98px;background:linear-gradient(135deg,#2e5a97,#3f78bf 50%,#1f4780)"></div>
  <div class="logo-mini" style="left:14px;top:14px"><i></i>VANTREL</div>
  <div class="abs" style="left:0;width:217px;top:56px;text-align:center;font-size:7px;font-weight:700;letter-spacing:1.2px">THANK YOU</div>
  <div class="abs navy" style="left:6px;top:104px;width:205px;height:14px"></div>
  <div class="abs" style="left:12px;top:108px;font-size:3px;color:#fff;display:flex;gap:12px">
    <span>12 Harbor Lane, Suite 4</span><span>hello@vantreladvisory.com</span><span>+1 (555) 010-2040</span><span>vantreladvisory.com</span>
  </div>
</section>

<!-- 20 Highlight -->
<section class="slide c5 r4">
  <div class="abs navy" style="left:6px;top:10px;width:205px;height:106px"></div>
  <div class="abs" style="left:98px;top:0;width:20px;height:20px;background:var(--blue)"></div>
  <div class="abs" style="left:104px;top:6px;width:8px;height:8px;border:1px solid #fff"></div>
  <div class="abs" style="left:0;width:217px;top:36px;text-align:center;font-size:7px;font-weight:600">The Highlight Headline</div>
  <div class="abs" style="left:34px;width:150px;top:52px;text-align:center;font-size:3.8px;line-height:5px;color:var(--pale)"><b style="color:#fff">Lorem ipsum dolor sit amet, consectetur adipiscing elit.</b> Brief supporting copy goes here in short lines to frame the key message of this highlight slide for readers.</div>
  <div class="abs" style="left:0;width:217px;top:84px;text-align:center;font-size:3px;color:var(--pale)">— cite the highlight source here</div>
  <div class="plus" style="left:178px;top:84px;background:#fff">+</div>
</section>
</main>

<footer class="specs">
  <span>16:9 (1920×1080)</span>
  <span>300dpi</span>
  <span>Fully editable in Powerpoint (.pptx/.pot)</span>
  <span>19 Master Slides</span>
  <span>Custom infographics</span>
</footer>

</body>
</html>
```